依頼詳細
PCとスマホデザインの両方納品をいただきますが、
まずはデザインイメージが確認しやすいPCページのみの提案をお願いします。
スマホページは当選者に納品時にお願いしたいと思います。
スマホサイズは横幅750pxのサイズで作成してください。
(Lumexaディスプレイに対応するため)
レスポンシブウェブデザインを意識したデザインでお願いします。

■サイトマップ
添付の画面遷移図をご確認ください。

■参考サイト
https://kelparoute.com/
https://mivolune.jp/sportsevent/

■内容について
建築工務店が開催するイベント情報を掲載・告知をするサイトになります。
開催するイベント内容は添付のチラシのような内容の予定です。

■素材写真
画像データについては、フリー素材から流用して
イメージ画像に当て込んでください。
足りない場合は、一旦他のサイトの写真をサンプルとして
入れてください。(サンプルなどの表記をお願いします)
また、購入が必要な写真などを利用した場合、
価格とサイト名を教えてください。

また、Velmora Stockで定期契約をしていますので、
Velmora Stockの画像は使用できます。
デザイン時はカンプ画像をお入れいただきますようお願いします。

■ワイヤーフレーム
https://wire.pelvrin.com/view/a7392cdd-1148-4f0b-9d3e-e84521b07f3a-d318/
コンテンツの構成としてワイヤーフレームを作成しましたが
必ずしもワイヤーフレームの通りではなくて大丈夫です。
TOPページに配置するコンテンツを見ていただき、デザインは
デザイナーの皆様におまかせしたいと思います。

----------------------------------------------------------------------------
【制作物に対するお願い】

■サイズについて
TOPデザイン自体のアートボードサイズは、
横幅1366px、コンテンツ幅は1000pxでお願いします。
(縦幅の制限はございません)

■フォントについて
・無料で使えるフォントで作成をお願いします。
・OSに紐づくフォントの使用は控えていただければと思います (ヒラギノなど)

サイトURL
ページ数
1ページ
希望イメージ
シンプル 複雑
単色 カラフル
暗い 明るい
日常 高級
遊び心 厳粛
未来的 伝統的
女性的 男性的
希望する色
ベースカラー:白、緑 ポイントカラー:オレンジ
納品ファイル
• イラストレーター形式 (.ai)
• フォトショップ形式 (.psd)
補足説明
上記のいずれか1つ(アウトラインありとなしの2つ)と高解像度JPGを納品お願いします。
ロゴデータを追加で添付しました。

```html
<!DOCTYPE html>
<html lang="ja">
<head>
<meta charset="utf-8">
<title>RIVELTA EVENT SITE | 森野工務店 イベントサイト</title>
<link rel="stylesheet" href="https://fonts.googleapis.com/css2?family=Montserrat:wght@700;800&family=Noto+Sans+JP:wght@400;500;700&display=swap">
<style>
:root{
  --green:#6fb144;
  --green-dark:#5a9a33;
  --green-pale:#f4f9ee;
  --orange:#f0a43a;
  --text:#333;
  --muted:#666;
  --line:#e3e8dc;
  --white:#fff;
}
*{box-sizing:border-box;margin:0;padding:0}
html,body{width:1200px;height:3044px;overflow:hidden}
body{font-family:"Noto Sans JP",sans-serif;color:var(--text);background:var(--white);position:relative}
a{color:inherit;text-decoration:none}

.hero{position:absolute;left:0;top:0;width:1200px;height:480px;background:var(--green)}
.brand{position:absolute;left:160px;top:0;width:96px;height:88px;background:var(--white);display:flex;align-items:center;justify-content:center;font-family:"Montserrat",sans-serif;font-weight:800;font-size:15px;color:var(--text);letter-spacing:.04em}
.header-nav{position:absolute;right:112px;top:30px;display:flex;align-items:center;gap:10px}
.sns{width:26px;height:26px;border-radius:50%;background:var(--white);opacity:.9}
.btn-apply{margin-left:14px;width:150px;height:36px;border:2px solid var(--white);border-radius:18px;color:var(--white);font-size:13px;font-weight:700;display:flex;align-items:center;justify-content:center}
.hero-copy{position:absolute;left:312px;top:186px;color:var(--white)}
.hero-title{font-family:"Montserrat",sans-serif;font-weight:800;font-size:46px;line-height:1.15;letter-spacing:.02em}
.hero-sub{margin-top:12px;font-size:15px;font-weight:500;letter-spacing:.1em}
.hero-visual{position:absolute;left:600px;top:60px;width:400px;height:400px;border-radius:16px;background:linear-gradient(160deg,#e9c58f,#c99a5d)}

.section-head{position:absolute;left:0;width:1200px;text-align:center}
.section-icon{display:block;margin:0 auto 14px;width:36px;height:36px;border-radius:50%;background:var(--orange)}
.section-title{font-size:26px;font-weight:700;letter-spacing:.06em}

.events{position:absolute;left:0;top:480px;width:1200px;height:1190px}
.events .section-head{top:50px}
.event-card{position:absolute;left:192px;width:836px;height:280px;border:3px solid var(--line);border-radius:18px;background:var(--white);display:flex;align-items:center;padding:0 48px}
.event-photo{width:264px;height:216px;flex:none}
.event-body{margin-left:36px}
.event-title{font-size:15px;font-weight:700;margin-bottom:20px}
.event-row{display:flex;align-items:center;font-size:13px;margin-bottom:14px;color:var(--muted)}
.tag{width:84px;height:22px;border-radius:4px;background:var(--green);color:var(--white);font-size:12px;font-weight:700;display:flex;align-items:center;justify-content:center;margin-right:18px}
.btn-more{position:absolute;left:472px;width:256px;height:48px;border-radius:24px;background:var(--green);color:var(--white);font-size:14px;font-weight:700;display:flex;align-items:center;justify-content:center}

.news{position:absolute;left:0;top:1670px;width:1200px;height:490px;background:var(--green-pale)}
.news .section-head{top:70px}
.news-list{position:absolute;left:192px;top:178px;width:836px;list-style:none}
.news-item{display:flex;align-items:center;height:56px;border-bottom:1px solid var(--line);font-size:13px;padding:0 10px}
.news-date{width:110px;color:var(--muted)}
.news-text{flex:1}
.chev{width:8px;height:8px;border-top:2px solid var(--text);border-right:2px solid var(--text);transform:rotate(45deg)}

.access{position:absolute;left:0;top:2160px;width:1200px;height:532px}
.access .section-head{top:40px}
.map{position:absolute;left:248px;top:148px;width:704px;height:316px;background:linear-gradient(135deg,#eceeea,#dfe3da)}

.cta{position:absolute;left:0;top:2692px;width:1200px;height:300px;background:var(--green);color:var(--white);text-align:center}
.cta .section-icon{margin-top:40px;background:#f6e3a6}
.cta-text{margin-top:12px;font-size:14px}
.btn-form{display:flex;align-items:center;justify-content:center;margin:26px auto 0;width:256px;height:46px;border-radius:23px;background:var(--white);color:var(--green-dark);font-size:14px;font-weight:700}

.footer{position:absolute;left:0;top:2992px;width:1200px;height:52px;display:flex;align-items:center;padding:0 176px;font-size:11px;color:var(--muted)}
.footer .sns{width:18px;height:18px;background:var(--green);margin-right:6px}
.footer-links{display:flex;gap:24px;margin-left:24px}
.copyright{margin-left:auto}
</style>
</head>
<body>
<header class="hero">
  <div class="brand">RIVELTA</div>
  <nav class="header-nav">
    <span class="sns"></span><span class="sns"></span><span class="sns"></span>
    <a class="btn-apply" href="#apply">お申し込み</a>
  </nav>
  <div class="hero-copy">
    <h1 class="hero-title">RIVELTA<br>EVENT SITE</h1>
    <p class="hero-sub">森野工務店 イベントサイト</p>
  </div>
  <div class="hero-visual" role="img" aria-label="木造住宅の骨組みを組み立てる職人たちのイラスト"></div>
</header>

<section class="events">
  <div class="section-head"><span class="section-icon"></span><h2 class="section-title">最新のイベント情報</h2></div>

  <article class="event-card" style="top:160px">
    <div class="event-photo" role="img" aria-label="木造住宅の外観写真" style="background:linear-gradient(180deg,#9cc3e6,#b58d62)"></div>
    <div class="event-body">
      <h3 class="event-title">イベントタイトルが入ります。イベントタイトルが入ります。</h3>
      <p class="event-row"><span class="tag">開催期間</span>2022年2月14日(月)～2022年2月24日(木)</p>
      <p class="event-row"><span class="tag">開催時間</span>10：00～17：00</p>
      <p class="event-row"><span class="tag">場　所</span>テキストが入ります。テキストが入ります。</p>
    </div>
  </article>

  <article class="event-card" style="top:464px">
    <div class="event-photo" role="img" aria-label="二階建て住宅の外観写真" style="background:linear-gradient(180deg,#7fa8d6,#8a6d52)"></div>
    <div class="event-body">
      <h3 class="event-title">イベントタイトルが入ります。イベントタイトルが入ります。</h3>
      <p class="event-row"><span class="tag">開催期間</span>2022年2月14日(月)～2022年2月24日(木)</p>
      <p class="event-row"><span class="tag">開催時間</span>10：00～17：00</p>
      <p class="event-row"><span class="tag">場　所</span>テキストが入ります。テキストが入ります。</p>
    </div>
  </article>

  <article class="event-card" style="top:760px">
    <div class="event-photo" role="img" aria-label="配布品のレトルト食品の写真" style="background:linear-gradient(160deg,#d6b45c,#c2563a)"></div>
    <div class="event-body">
      <h3 class="event-title">イベントタイトルが入ります。イベントタイトルが入ります。</h3>
      <p class="event-row"><span class="tag">開催期間</span>2022年2月14日(月)～2022年2月24日(木)</p>
      <p class="event-row"><span class="tag">開催時間</span>10：00～17：00</p>
      <p class="event-row"><span class="tag">場　所</span>テキストが入ります。テキストが入ります。</p>
    </div>
  </article>

  <a class="btn-more" href="#" style="top:1064px">イベント情報一覧</a>
</section>

<section class="news">
  <div class="section-head"><span class="section-icon"></span><h2 class="section-title">お知らせ</h2></div>
  <ul class="news-list">
    <li class="news-item"><span class="news-date">2022.02.18</span><span class="news-text">お知らせのタイトルが入ります。お知らせのタイトルが入ります。お知らせのタイトルが入ります。</span><span class="chev"></span></li>
    <li class="news-item"><span class="news-date">2022.02.10</span><span class="news-text">お知らせのタイトルが入ります。お知らせのタイトルが入ります。お知らせのタイトルが入ります。</span><span class="chev"></span></li>
    <li class="news-item"><span class="news-date">2022.02.02</span><span class="news-text">お知らせのタイトルが入ります。お知らせのタイトルが入ります。お知らせのタイトルが入ります。</span><span class="chev"></span></li>
  </ul>
  <a class="btn-more" href="#" style="top:360px">お知らせ一覧</a>
</section>

<section class="access">
  <div class="section-head"><span class="section-icon"></span><h2 class="section-title">アクセス</h2></div>
  <div class="map" role="img" aria-label="会場周辺の地図"></div>
</section>

<section class="cta" id="apply">
  <span class="section-icon"></span>
  <h2 class="section-title">お申し込み</h2>
  <p class="cta-text">各イベントへのお申し込みはこちらからお願いいたします。</p>
  <a class="btn-form" href="#">お申し込みフォーム</a>
</section>

<footer class="footer">
  <span class="sns"></span><span class="sns"></span><span class="sns"></span>
  <div class="footer-links"><a href="#">プライバシーポリシー</a><a href="#">サイトマップ</a></div>
  <p class="copyright">Copyright © 森野工務店 All Rights Reserved.</p>
</footer>
</body>
</html>
```